BrightLaneNest.Com needs a email flyer to be sent to Realtors about our awesome mortgage services!

We are a real estate and mortgage company. This flyer will advertise the USPs of our mortgage services to Realtors. The intent is for these Realtors to contact us and then have their buyer clients contact us for a real estate mortgage loan.
The flyer will be email blasted to Realtors.
Size is 8.5 x 11 inches i.e. US Letter size. (Portrait in Orientation)
***This is an eFlyer and will be delivered by email, it is not a print flyer.
IN THE ATTACHMENT you'll find the text needed in the flyer.
For theme colors and added details you may go to our website:
www.brightlanenest.com
Industry/Entity Type
Real Estate
Look and feel

```html
<!DOCTYPE html>
<html lang="en">
<head>
<meta charset="utf-8">
<title>BrightLaneNest.Com – Realtor Referral eFlyer</title>
<link rel="stylesheet" href="https://fonts.googleapis.com/css2?family=Roboto+Condensed:wght@300;400;700&family=Lato:wght@400;700&display=swap">
<style>
  :root{
    --green:#7cc242;
    --green-dark:#4f9a2c;
    --blue:#1ba3e0;
    --charcoal:#454545;
    --ink:#222;
    --page:#e6e6e6;
    --white:#fff;
  }
  *{box-sizing:border-box;margin:0;padding:0}
  html,body{width:806px;height:1200px;overflow:hidden;background:var(--page)}
  .flyer{
    position:absolute;left:20px;top:108px;width:655px;height:840px;
    transform:scale(1.17);transform-origin:0 0;background:var(--white);
    box-shadow:0 2px 8px rgba(0,0,0,.25);overflow:hidden;
    font-family:"Lato",sans-serif;color:var(--ink);
  }
  .hero{position:absolute;left:0;top:0;width:655px;height:443px;display:block}

  .brand{position:absolute;left:25px;top:30px;display:flex;align-items:center;gap:9px}
  .brand-mark{width:14px;height:14px;background:var(--green)}
  .brand-name{font-family:"Lato",sans-serif;font-weight:700;font-size:21px;line-height:1;color:var(--charcoal)}
  .brand-tagline{position:absolute;left:25px;top:57px;font-family:"Lato",sans-serif;font-weight:700;font-size:10.5px;color:var(--charcoal)}

  .headline-band{position:absolute;left:0;top:443px;width:655px;height:97px;background:var(--charcoal);padding:12px 15px 0}
  .headline-primary{font-family:"Roboto Condensed",sans-serif;font-weight:700;font-size:30px;color:var(--green);line-height:1.05;letter-spacing:-.2px;white-space:nowrap}
  .headline-secondary{font-family:"Roboto Condensed",sans-serif;font-weight:300;font-size:34.5px;color:var(--white);line-height:1.2;letter-spacing:.2px;white-space:nowrap}

  .rate-column{position:absolute;left:0;top:540px;width:393px;height:252px}
  .rate-tab{position:absolute;left:0;top:12px;width:212px;height:30px;background:var(--blue);
    clip-path:polygon(0 0,100% 0,90% 100%,0 100%);
    font-family:"Roboto Condensed",sans-serif;font-weight:700;font-size:15.5px;color:var(--white);padding:6px 0 0 15px}
  .rate-list{position:absolute;left:15px;top:50px;list-style:none;font-weight:700;font-size:12.2px;line-height:15px;color:var(--ink)}
  .rate-list li{padding-left:11px;position:relative}
  .rate-list li::before{content:"";position:absolute;left:0;top:5px;width:5px;height:5px;border-radius:50%;background:var(--blue)}
  .rate-promise{position:absolute;left:15px;top:143px;font-family:"Roboto Condensed",sans-serif;font-weight:700;line-height:1.15;white-space:nowrap}
  .rate-promise .line-blue{color:var(--blue);font-size:15.5px}
  .rate-promise .line-green{color:var(--green-dark);font-size:19.5px;letter-spacing:.4px}
  .disclaimer{position:absolute;left:15px;top:216px;width:370px;font-size:6.6px;line-height:8px;color:#333}

  .divider{position:absolute;left:393px;top:540px;width:7px;height:252px;background:var(--blue)}
  .referral-column{position:absolute;left:402px;top:540px;width:253px;height:252px;
    background:linear-gradient(150deg,#8fd14f 0%,var(--green) 45%,var(--green-dark) 100%);padding:10px 12px 0 12px;color:var(--white)}
  .referral-heading{font-family:"Roboto Condensed",sans-serif;font-weight:700;line-height:1.1;border-bottom:1px solid rgba(255,255,255,.8);padding-bottom:4px}
  .referral-heading .h1{font-size:15.5px;letter-spacing:.6px}
  .referral-heading .h2{font-size:15px;font-weight:400}
  .referral-heading .h3{font-size:22px;font-weight:400}
  .referral-list{list-style:none;margin-top:10px;font-weight:700;font-size:11.6px;line-height:14.5px;color:#1d2a12}
  .referral-list li{position:relative;padding-left:16px;margin-bottom:9px}
  .referral-list li::before{content:"";position:absolute;left:0;top:3px;width:7px;height:7px;border-radius:50%;background:var(--white);border:2px solid var(--blue)}

  .contact-bar{position:absolute;left:0;top:792px;width:655px;height:48px;background:var(--charcoal);color:var(--white)}
  .call{position:absolute;left:18px;top:12px;font-family:"Lato",sans-serif;font-weight:700;font-size:18px;white-space:nowrap}
  .call .name{color:var(--green)}
  .contact-links{position:absolute;left:395px;top:6px;font-weight:700;font-size:11.5px;line-height:17px;white-space:nowrap}
  .contact-links div{display:flex;align-items:center;gap:6px}
  .contact-links svg{width:9px;height:9px;fill:var(--green)}
</style>
</head>
<body>
<div class="flyer">
  <svg class="hero" viewBox="0 0 655 443">
    <defs>
      <linearGradient id="houseTone" x1="0" y1="0" x2="0" y2="1">
        <stop offset="0" stop-color="#3f6fb8"/>
        <stop offset=".35" stop-color="#8fa7c4"/>
        <stop offset=".6" stop-color="#9a8a78"/>
        <stop offset="1" stop-color="#5f6b3e"/>
      </linearGradient>
      <linearGradient id="coupleTone" x1="0" y1="0" x2="1" y2="1">
        <stop offset="0" stop-color="#f4efe6"/>
        <stop offset=".5" stop-color="#d9b7a0"/>
        <stop offset="1" stop-color="#9ccbe0"/>
      </linearGradient>
    </defs>
    <polygon fill="var(--green)" points="0,85 78,270 0,360"/>
    <polygon fill="var(--green)" points="655,88 595,275 655,372"/>
    <polygon fill="var(--green)" points="330,62 655,370 655,443 0,443 0,353"/>
    <polygon fill="var(--blue)" points="330,72 655,386 655,443 0,443 0,370"/>
    <polygon fill="url(#houseTone)" points="330,94 655,404 655,443 0,443 0,392"
      role="img" aria-label="Photo of a large brick family home with arched windows and trees"/>
    <rect x="478" y="18" width="177" height="255" fill="url(#coupleTone)"
      role="img" aria-label="Photo of a smiling couple embracing"/>
  </svg>

  <div class="brand">
    <div class="brand-mark"></div>
    <div class="brand-name">BrightLaneNest.Com</div>
  </div>
  <div class="brand-tagline">Your Local Home Loan Team</div>

  <section class="headline-band">
    <h1 class="headline-primary">GET MORE REFERRALS FROM YOUR BUYER CLIENTS</h1>
    <h2 class="headline-secondary">BE A SUPER HERO BUYERS AGENT</h2>
  </section>

  <section class="rate-column">
    <div class="rate-tab">DREAM INTEREST RATE</div>
    <ul class="rate-list">
      <li>We are meeting deadlines, closing and funding<br>on time, originating loans since 2001</li>
      <li>Today's rate 3.75%</li>
      <li>Today's closing cost credit</li>
      <li>Hollingsworth of service and the PennySave of rates</li>
    </ul>
    <div class="rate-promise">
      <div class="line-blue">REMEMBER WE ARE HOLLINGSWORTH OF SERVICE</div>
      <div class="line-green">AND THE PENNYSAVE OF RATES</div>
    </div>
    <p class="disclaimer">Not for consumer use, for Mortgage and Real Estate Professionals ONLY. This does not meet TILA or RESPA requirements for advertising.</p>
  </section>

  <div class="divider"></div>

  <section class="referral-column">
    <div class="referral-heading">
      <div class="h1">MAXIMIZE YOUR REFERRAL</div>
      <div class="h2">from your clients when you refer</div>
      <div class="h3">them to a lender who</div>
    </div>
    <ul class="referral-list">
      <li>Will encourage them to shop</li>
      <li>Offer them mortgage rates com<br>parable to internet lenders</li>
      <li>Offer super low OR NO closing costs<br>comparable to internet lenders</li>
      <li>Is a local lender and your clients can<br>meet in person</li>
    </ul>
  </section>

  <footer class="contact-bar">
    <div class="call"><span class="name">Call Marcus Delaney</span> 555-014-2290</div>
    <div class="contact-links">
      <div><svg viewBox="0 0 10 10"><path d="M0 2h10v6H0z M0 2l5 3.5L10 2"/></svg>Marcus@BrightLaneNest.Com</div>
      <div><svg viewBox="0 0 10 10"><circle cx="5" cy="5" r="5"/></svg>www.brightlanenest.com</div>
    </div>
  </footer>
</div>
</body>
</html>
```